Biz Card for Harrowfield Property Partners - HWPP

Harrowfield Property Partners is a commercial real estate acquisitions firm. We buy commercial property and need to raise capital from investors for each deal we buy. The vibe needs to be: give us your money, we will multiply it.
Our website: www.hrwpp-example.com
Competitors are: https://velmarholdings-example.com/, https://tribanquepartners-example.com/, http://www.ostrellecapital-example.com/
Target Market(s)
High Net Worth Individuals, Bankers, Insurance Companies, Commercial Real Estate Brokers.
Industry/Entity Type
Investment Banking
Contact Information for Business Card
Name, Title, Addess, Cell#, Office#, email, website
Requirements
Must have
- use one of our logos. See website for look and feel: www.hrwpp-example.com
Nice to have
- see website: www.hrwpp-example.com

```html
<!DOCTYPE html>
<html lang="en">
<head>
<meta charset="utf-8">
<title>Harrowfield Property Partners – Business Card</title>
<link href="https://fonts.googleapis.com/css2?family=Inter:wght@400;700&display=swap" rel="stylesheet">
<style>
  :root {
    --backdrop: #3aaebf;
    --navy: #1e2a3f;
    --navy-deep: #0f2a44;
    --gold: #bb9a6f;
    --paper: #ffffff;
    --ink: #1e2a3f;
  }
  * { box-sizing: border-box; margin: 0; padding: 0; }
  html, body {
    width: 1200px; height: 1200px; overflow: hidden;
    background: var(--backdrop);
    font-family: "Inter", Arial, sans-serif;
  }
  .canvas { position: relative; width: 1200px; height: 1200px; }
  .card {
    position: absolute; left: 337px; width: 526px; height: 300px;
    background: var(--paper); overflow: hidden;
  }
  .card--front { top: 256px; }
  .card--back { top: 622px; }

  .front__header {
    position: absolute; left: 0; top: 0; width: 100%; height: 150px;
    background: var(--navy);
  }
  .front__rule {
    position: absolute; left: 0; top: 150px; width: 100%; height: 10px;
    background: var(--gold);
  }
  .front__name {
    position: absolute; left: 45px; top: 47px;
    color: var(--paper); font-weight: 700; font-size: 24px; letter-spacing: -0.3px;
  }
  .front__title {
    position: absolute; left: 45px; top: 76px;
    color: var(--paper); font-weight: 400; font-size: 16px;
  }
  .contact-list {
    position: absolute; left: 42px; top: 177px; list-style: none;
  }
  .contact-list__item {
    display: flex; align-items: center; height: 24.3px;
    color: var(--ink); font-size: 16px; white-space: nowrap;
  }
  .contact-list__icon { width: 16px; height: 16px; margin-right: 12px; flex: none; }

  .back__mark {
    position: absolute; left: 215px; top: 64px; width: 96px; height: 96px;
    border-radius: 50%; background: var(--navy-deep);
  }
  .back__name {
    position: absolute; left: 0; width: 100%; text-align: center;
    color: var(--navy-deep); font-weight: 400; white-space: nowrap;
  }
  .back__name--main { top: 166px; font-size: 38px; letter-spacing: 8px; padding-left: 8px; }
  .back__name--sub { top: 216px; font-size: 16px; letter-spacing: 8px; padding-left: 8px; }
</style>
</head>
<body>
<main class="canvas">
  <section class="card card--front">
    <div class="front__header"></div>
    <div class="front__rule"></div>
    <h1 class="front__name">Marcus Ellery Dunmore</h1>
    <p class="front__title">Managing Partner, Acquisitions</p>
    <ul class="contact-list">
      <li class="contact-list__item">
        <svg class="contact-list__icon" viewBox="0 0 24 24"><path fill="var(--ink)" d="M6.6 10.8a15.1 15.1 0 0 0 6.6 6.6l2.2-2.2c.3-.3.7-.4 1-.2 1.1.4 2.3.6 3.6.6.6 0 1 .4 1 1V20c0 .6-.4 1-1 1C10.6 21 3 13.4 3 4c0-.6.4-1 1-1h3.5c.6 0 1 .4 1 1 0 1.3.2 2.5.6 3.6.1.3 0 .7-.2 1z"/></svg>
        Cell (555) 210-4387 · Office (555) 210-4300
      </li>
      <li class="contact-list__item">
        <svg class="contact-list__icon" viewBox="0 0 24 24"><path fill="var(--ink)" d="M12 3 2 12h3v9h5v-6h4v6h5v-9h3z"/></svg>
        48 Larkspur Ave, Suite 900 Westbrook, FL 33000
      </li>
      <li class="contact-list__item">
        <svg class="contact-list__icon" viewBox="0 0 24 24" fill="none" stroke="var(--ink)" stroke-width="1.5"><circle cx="12" cy="12" r="9.5"/><ellipse cx="12" cy="12" rx="4" ry="9.5"/><path d="M2.5 12h19M4 7h16M4 17h16"/></svg>
        www.hrwpp-example.com
      </li>
      <li class="contact-list__item">
        <svg class="contact-list__icon" viewBox="0 0 24 24"><path fill="var(--ink)" d="M2 6h20v12H2z"/><path fill="none" stroke="var(--paper)" stroke-width="1.4" d="M2.5 6.5 12 13l9.5-6.5M2.5 17.5l7-6M21.5 17.5l-7-6"/></svg>
        team@hrwpp-example.com
      </li>
    </ul>
  </section>

  <section class="card card--back">
    <div class="back__mark"></div>
    <p class="back__name back__name--main">HARROWFIELD</p>
    <p class="back__name back__name--sub">PROPERTY PARTNERS</p>
  </section>
</main>
</body>
</html>
```